Creative Business Card

Were looking for a new fresh and creative look to our Business card. Our company name is InkVale. Be creative, Were attaching our logo and our base colors, but your free to do anything. Name, title, Phone

Industry/Entity Type

Business

```html
<!DOCTYPE html>
<html lang="en">
<head>
<meta charset="utf-8">
<title>InkVale Business Cards</title>
<link rel="stylesheet" href="https://fonts.googleapis.com/css2?family=Open+Sans:wght@400;600;700;800&display=swap">
<style>
  :root {
    --backdrop: #4a3628;
    --brand-green: #8cc63f;
    --brand-blue: #1b8fd2;
    --ink-dark: #3a3a3a;
    --ink-mid: #555555;
    --band-black: #0c0c0c;
    --silver-light: #ffffff;
    --silver-mid: #e6e6e6;
    --silver-edge: #c9c9c9;
    --night-core: #173650;
    --night-edge: #05090e;
    --white: #ffffff;
  }
  * { margin: 0; padding: 0; box-sizing: border-box; }
  html, body { width: 1200px; height: 810px; overflow: hidden; }
  body {
    background: var(--backdrop);
    font-family: "Open Sans", Arial, sans-serif;
    position: relative;
  }
  .card {
    position: absolute;
    width: 497px;
    height: 282px;
    box-shadow: 0 6px 16px rgba(0,0,0,0.45);
    overflow: hidden;
  }
  .card--silver {
    background: linear-gradient(100deg, var(--silver-edge) 0%, var(--silver-light) 35%, var(--silver-mid) 65%, var(--silver-edge) 100%);
  }
  .card--night {
    background: radial-gradient(ellipse at 50% 40%, var(--night-core) 0%, #0c1c2b 45%, var(--night-edge) 85%);
  }
  .card--front { left: 82px; top: 98px; }
  .card--back-light { left: 605px; top: 94px; }
  .card--back-dark { left: 350px; top: 416px; }

  .brand {
    position: absolute;
    left: 0; right: 0;
    display: flex;
    justify-content: center;
    align-items: center;
    gap: 12px;
  }
  .brand__mark {
    width: 30px; height: 30px;
    background: var(--brand-blue);
  }
  .brand__name {
    font-weight: 800;
    font-size: 58px;
    line-height: 1;
    color: var(--brand-green);
    letter-spacing: 0.5px;
  }
  .card--front .brand { top: 34px; }
  .card--back-light .brand,
  .card--back-dark .brand { top: 92px; }

  .holder {
    position: absolute;
    top: 148px; left: 0; right: 0;
    text-align: center;
    font-size: 17px;
    color: var(--ink-dark);
  }
  .holder__name { font-weight: 600; }
  .holder__divider { color: #999; margin: 0 4px; }
  .holder__title { font-size: 13px; letter-spacing: 0.8px; color: var(--ink-mid); }

  .contact-band { position: absolute; left: 0; top: 213px; width: 497px; height: 28px; }
  .contact-band__address {
    position: absolute; left: 26px; top: 218px;
    font-size: 13px; color: var(--white);
  }
  .contact-band__web {
    position: absolute; right: 30px; top: 216px;
    font-size: 14px; font-weight: 700; color: var(--white); letter-spacing: 0.6px;
  }
  .contact-line {
    position: absolute; top: 250px; left: 0; right: 0;
    text-align: center; font-size: 12px; color: var(--ink-dark);
  }
  .contact-line__label { color: var(--brand-blue); }
  .contact-line__sep { margin: 0 6px; }

  .web {
    position: absolute; top: 176px; left: 0; right: 0;
    text-align: center; font-size: 13px; letter-spacing: 2.4px;
  }
  .card--back-light .web { color: var(--ink-dark); }
  .card--back-dark .web { color: #d8dde2; }
</style>
</head>
<body>

  <section class="card card--silver card--front">
    <div class="brand">
      <span class="brand__name">InkVale</span>
    </div>
    <p class="holder">
      <span class="holder__name">YOUR NAME</span><span class="holder__divider">|</span><span class="holder__title">DIRECTOR</span>
    </p>
    <svg class="contact-band" viewBox="0 0 497 28" aria-hidden="true">
      <polygon points="0,2 308,2 298,28 0,28" fill="var(--brand-blue)"/>
      <polygon points="312,0 497,0 497,27 300,27" fill="var(--band-black)"/>
    </svg>
    <span class="contact-band__address">PO Box 01234, Cityname,Country name</span>
    <span class="contact-band__web">www.inkvale.com</span>
    <p class="contact-line">
      <span class="contact-line__label">P :</span> 012 345 6789<span class="contact-line__sep">|</span><span class="contact-line__label">M :</span> 012 345 6789<span class="contact-line__sep">|</span><span class="contact-line__label">E :</span> info@inkvale.com
    </p>
  </section>

  <section class="card card--silver card--back-light">
    <div class="brand">
      <span class="brand__name">InkVale</span>
    </div>
    <p class="web">www.inkvale.com</p>
  </section>

  <section class="card card--night card--back-dark">
    <div class="brand">
      <span class="brand__name">InkVale</span>
    </div>
    <p class="web">www.inkvale.com</p>
  </section>

</body>
</html>
```